fernvale junk clearing

A 6 flyer design.......
I have up loaded our company logo ....must use
A location map...........must use
and our business card with our contact information......please add all contact info
our ph. number must bold and prominent feature.....use use

A reliable Asbestos Removal & Demolition service that you can trust. All our services are offered at realistic prices and delivered on time. We operate 24 / 7 and provide free no-obligation quotes with good old fashion service.

We service the following towns and surrounding areas 7
days a week & 24 hours
Kempsey
Taree
South West Rocks
foster / Tuncurry
Coffs harbour
Nambucca Heads
Newcastle
Maitland
Singleton
Muswellbrook
Upper Hunter Valley
Central Coast
Tamworth
Armidale
this is an easy design as I have most of the theme and colours

```html
<!DOCTYPE html>
<html lang="en">
<head>
<meta charset="utf-8">
<title>Fernvale Junk Clearing – Flyer</title>
<link rel="stylesheet" href="https://fonts.googleapis.com/css2?family=PT+Sans:wght@400;700&display=swap">
<style>
  :root {
    --green-deep: #0a8a4a;
    --green-mid: #21a35a;
    --green-pale: #a9dfc0;
    --mint: #cdeedd;
    --yellow: #ffe100;
    --lime-text: #d8f500;
    --outline: #138a2e;
    --earth-1: #8a7445;
    --earth-2: #6c6a3a;
    --map-land: #e9efdd;
    --map-sea: #a8cdee;
  }
  * { box-sizing: border-box; margin: 0; padding: 0; }
  html, body { width: 1200px; height: 1003px; overflow: hidden; background: #ffffff; }
  body { font-family: "PT Sans", sans-serif; position: relative; }
  .canvas-frame { position: absolute; inset: 0; border: 1px solid #555; pointer-events: none; }
  .flyer { position: absolute; left: 222px; top: 0; width: 773px; height: 1003px; overflow: hidden; }

  .outlined {
    color: var(--yellow);
    -webkit-text-stroke: 1.2px var(--outline);
    paint-order: stroke fill;
  }

  /* header */
  .header {
    position: absolute; left: 0; top: 0; width: 773px; height: 310px;
    background: linear-gradient(90deg, var(--green-deep) 0%, #ffffff 16%, #ffffff 84%, var(--green-deep) 100%);
  }
  .brand { position: absolute; left: 0; right: 0; top: 40px; display: flex; align-items: center; justify-content: center; gap: 22px; }
  .brand-square { width: 120px; height: 120px; border-radius: 14px; background: var(--yellow); border: 3px solid var(--green-mid); }
  .brand-name { font-weight: 700; font-size: 54px; line-height: 1.05; color: var(--green-mid); text-transform: uppercase; }
  .contact-line { position: absolute; left: 0; right: 0; top: 262px; text-align: center; font-size: 35px; font-weight: 700; letter-spacing: -0.5px; }

  .stripe { position: absolute; left: 0; width: 773px; background: var(--green-pale); }
  .stripe.top { top: 310px; height: 15px; }
  .stripe.mid { top: 550px; height: 17px; }

  /* intro over photo */
  .intro { position: absolute; left: 0; top: 325px; width: 773px; height: 225px; }
  .intro-photo { position: absolute; inset: 0; background: linear-gradient(100deg, var(--earth-2), var(--earth-1) 45%, #7d6b43 70%, #5f6a3e); }
  .intro-copy { position: absolute; left: 56px; width: 663px; top: 16px; text-align: justify; font-size: 22.5px; line-height: 33px; color: var(--lime-text); -webkit-text-stroke: 1px var(--outline); paint-order: stroke fill; }
  .intro-copy p + p { margin-top: 10px; line-height: 28px; }

  /* service area */
  .service { position: absolute; left: 0; top: 567px; width: 773px; height: 436px;
    background: linear-gradient(180deg, var(--mint) 0%, #7fd0a8 55%, var(--green-mid) 100%); }
  .hours { position: absolute; left: 91px; top: 10px; font-size: 40px; font-weight: 700; line-height: 40px; letter-spacing: -0.5px; }
  .towns { position: absolute; left: 91px; top: 108px; font-size: 16.5px; font-weight: 700; line-height: 22.3px; letter-spacing: -0.3px; list-style: none; }
  .phone { position: absolute; left: 89px; top: 265px; font-size: 56px; font-weight: 700; letter-spacing: -0.5px; }
  .map { position: absolute; left: 447px; top: 0; width: 326px; height: 323px;
    background: linear-gradient(90deg, var(--map-land) 0%, #dfe9cf 70%, var(--map-sea) 85%); }

  .bar { position: absolute; left: 0; width: 773px; background: linear-gradient(180deg, #1da65a, var(--green-deep)); border-top: 3px solid #58c48a; text-align: center; font-size: 35px; }
  .bar.email { top: 890px; height: 56px; line-height: 54px; }
  .bar.web { top: 946px; height: 57px; line-height: 58px; }
</style>
</head>
<body>
  <div class="flyer">
    <header class="header">
      <div class="brand">
        <div class="brand-square"></div>
        <div class="brand-name">Fernvale<br>Junk Clearing</div>
      </div>
      <p class="contact-line outlined">Liam Hartley | Site Supervisor | 0491 570 226</p>
    </header>

    <div class="stripe top"></div>

    <section class="intro">
      <div class="intro-photo" role="img" aria-label="Photograph of a demolition site with rubble in front of a partly torn-down building"></div>
      <div class="intro-copy">
        <p>A reliable Asbestos Removal &amp; Demolition service that you can trust. All our services are offered at realistic prices and delivered on time. We operate 24 / 7 and provide free no-obligation quotes with good old fashion service.</p>
        <p>Australian owned &amp; operated, fully licenced &amp; insured, a trusted local name! Servicing the mid north coast and beyond...</p>
      </div>
    </section>

    <div class="stripe mid"></div>

    <section class="service">
      <h2 class="hours outlined">24 hours a day<br>7 days a week</h2>
      <ul class="towns outlined">
        <li>Kempsey | Taree | South West Rocks</li>
        <li>Foster / Tuncurry | Coffs harbour</li>
        <li>Nambucca Heads | Newcastle</li>
        <li>Maitland | Singleton | Muswellbrook</li>
        <li>Upper Hunter Valley | Central Coast</li>
        <li>Tamworth | Armidale</li>
      </ul>
      <p class="phone outlined">0491 570 226</p>
      <div class="map" role="img" aria-label="Road map of the New South Wales mid north coast with a circle marking the service area"></div>
    </section>

    <div class="bar email outlined">fernvalejunkclearing@postbox.net</div>
    <div class="bar web outlined">www.fernvalejunkclearing.com</div>
  </div>
  <div class="canvas-frame"></div>
</body>
</html>
```